Harbourline construction company Business card design

I need a business card design for my company. I have a logo but dont have business cards with our logo..

www.harbourlineconstructco.com.au

The logo is on the website

I need the same details as this design I have attached. we have changed the logo and colours. just like the website

Industry/Entity Type

Building

```html
<!DOCTYPE html>
<html lang="en">
<head>
<meta charset="utf-8">
<title>Harbourline Construction – Business Card</title>
<link rel="stylesheet" href="https://fonts.googleapis.com/css2?family=Fira+Sans+Condensed:wght@300;400;600&display=swap">
<style>
  :root {
    --backdrop: #2c2c2c;
    --card-white: #ffffff;
    --brand-blue: #1b7fc0;
    --blue-line: #5aa6d8;
    --muted-blue: #bfdcf1;
    --text-grey: #6f7276;
    --text-white: #ffffff;
  }
  * { margin: 0; padding: 0; box-sizing: border-box; }
  html, body {
    width: 1200px;
    height: 799px;
    overflow: hidden;
    background: var(--backdrop);
    font-family: "Fira Sans Condensed", "Arial Narrow", sans-serif;
  }
  .business-card {
    position: absolute;
    left: 105px;
    top: 97px;
    width: 990px;
    height: 605px;
    background: var(--card-white);
    overflow: hidden;
  }
  .card-background {
    position: absolute;
    inset: 0;
    width: 100%;
    height: 100%;
  }
  .brand {
    position: absolute;
    left: 70px;
    top: 90px;
    color: var(--brand-blue);
  }
  .brand-square {
    width: 34px;
    height: 34px;
    background: var(--brand-blue);
    margin-bottom: 22px;
  }
  .brand-name {
    font-weight: 400;
    font-size: 50px;
    line-height: 1.02;
    letter-spacing: 1px;
    text-transform: uppercase;
  }
  .services {
    position: absolute;
    left: 66px;
    top: 372px;
    list-style: none;
    color: var(--text-grey);
    font-weight: 300;
    font-size: 23px;
    line-height: 1.45;
  }
  .services li::before {
    content: "•";
    color: var(--brand-blue);
    margin-right: 7px;
  }
  .contact-panel {
    position: absolute;
    right: 78px;
    top: 170px;
    text-align: right;
    color: var(--text-white);
  }
  .person-name {
    font-weight: 600;
    font-size: 36px;
    letter-spacing: 0.5px;
    text-transform: uppercase;
  }
  .person-role {
    font-weight: 300;
    font-size: 25px;
    color: var(--muted-blue);
    margin-top: 2px;
  }
  .contact-list {
    list-style: none;
    margin-top: 74px;
    font-weight: 400;
    font-size: 26px;
    line-height: 1.36;
  }
  .contact-label { font-weight: 600; }
</style>
</head>
<body>
  <article class="business-card">
    <svg class="card-background" viewBox="0 0 990 605" aria-hidden="true">
      <polygon points="594,0 990,0 990,605 376,605" fill="var(--brand-blue)"/>
      <line x1="612" y1="0" x2="394" y2="605" stroke="var(--blue-line)" stroke-width="2"/>
    </svg>

    <div class="brand">
      <div class="brand-square"></div>
      <div class="brand-name">Harbourline<br>Construction</div>
    </div>

    <ul class="services">
      <li>New Homes</li>
      <li>Additions &amp; Renovations</li>
      <li>Domestic &amp; Commercial Builders</li>
    </ul>

    <div class="contact-panel">
      <h1 class="person-name">Marcus Delane</h1>
      <p class="person-role">Director</p>
      <ul class="contact-list">
        <li><span class="contact-label">p:</span> 08 9400 1187</li>
        <li><span class="contact-label">m:</span> 0412 558 901</li>
        <li><span class="contact-label">e:</span> info@harbourlineconstructco.com.au</li>
        <li>www.harbourlineconstructco.com.au</li>
      </ul>
    </div>
  </article>
</body>
</html>
```